E-Commerce Custom Design Magento Standard Requirements For Marketing Agency

I need to revamp theme for a website www.plinthwavestudio.com and want to change name to www.plinthwavehomes.com I have logo attached. I need a custom e commerce website built that pops and grabs attention. My logo is silver and looks great on black background. Please just use all same content from existing website www.plinthwavestudio.com and use existing products that you see there.

Target Market(s)

REAL ESTATE AGENTS

Industry/Entity Type

Digital Marketing

Coding

Coded - Design and coding required

Number of Pages Required

5+ page

Colors

Designer to choose colors to be used in the design.

Requirements
Must have
• Please revamp entire website www.plinthwavestudio.com and use new logo attached. Domain name will be www.plinthwavehomes.com and will offer marketing services for real estate agents around the country and world. Specializing in digital marketing services such as Vellumly Ads, Pictoraze Ads, Quip Loop Ads, Zarbit Promoworks, Etc.
Nice to have
Should not have

```html
<!DOCTYPE html>
<html lang="en">
<head>
<meta charset="utf-8">
<title>Contact Us – Plinthwave</title>
<link href="https://fonts.googleapis.com/css2?family=Oswald:wght@300;400&family=Playfair+Display:wght@700&family=Source+Sans+3:wght@400;600&family=EB+Garamond&family=Arimo&display=swap" rel="stylesheet">
<style>
  :root {
    --teal: #20c7bd;
    --white: #ffffff;
    --ink: #222222;
    --field: #e9e9e9;
    --submit: #e8533f;
    --chat: #3cbf72;
    --footer: #111111;
    --badge: #e8533f;
    --map-land: #e8e6e1;
    --map-water: #aadaff;
  }
  * { box-sizing: border-box; margin: 0; padding: 0; }
  html, body { width: 1200px; height: 1027px; overflow: hidden; background: var(--white); }
  .page { position: relative; width: 1200px; height: 1027px; overflow: hidden; font-family: "Source Sans 3", sans-serif; color: var(--ink); }
  .abs { position: absolute; }

  .site-header { position: absolute; left: 0; top: 0; width: 1200px; height: 94px; background: var(--teal); }
  .brand { left: 140px; top: 34px; display: flex; align-items: center; gap: 6px; color: var(--white); font-family: "Oswald", sans-serif; font-weight: 400; font-size: 17px; letter-spacing: 1px; }
  .brand-mark { width: 12px; height: 12px; border-radius: 50%; background: var(--white); }
  .header-phone { left: 336px; top: 28px; font-family: "Oswald", sans-serif; font-weight: 300; font-size: 32px; color: var(--white); line-height: 1; }
  .cart { left: 600px; top: 36px; }
  .cart-badge { left: 638px; top: 32px; width: 17px; height: 17px; border-radius: 50%; background: var(--badge); color: var(--white); font-size: 11px; text-align: center; line-height: 17px; }
  .main-nav a { position: absolute; top: 40px; font-family: "Oswald", sans-serif; font-weight: 300; font-size: 21px; color: var(--white); text-decoration: none; }
  .user { left: 964px; top: 32px; }
  .user-name { left: 998px; top: 38px; font-family: "EB Garamond", serif; font-size: 13px; color: var(--white); }

  .page-title { left: 0; width: 1200px; top: 114px; text-align: center; font-family: "Playfair Display", serif; font-size: 38px; color: var(--ink); }
  .title-rule { left: 510px; top: 162px; width: 180px; height: 2px; background: var(--ink); }

  .map { left: 0; top: 221px; width: 1200px; height: 350px; background: linear-gradient(90deg, var(--map-water) 0%, var(--map-water) 34%, var(--map-land) 40%, var(--map-land) 100%); }
  .address-card { left: 933px; top: 382px; width: 229px; height: 158px; background: var(--teal); color: var(--white); font-family: "Arimo", sans-serif; }
  .address-card h3 { position: absolute; left: 22px; top: 20px; font-family: "Source Sans 3", sans-serif; font-weight: 400; font-size: 21px; }
  .address-card p { position: absolute; left: 34px; top: 72px; font-size: 10px; line-height: 16px; }
  .address-tail { left: 933px; top: 539px; }

  .field { background: var(--field); font-size: 17px; padding: 3px 5px; color: var(--ink); }
  .submit { left: 388px; top: 782px; width: 97px; height: 32px; background: var(--submit); color: var(--white); font-weight: 600; font-size: 20px; text-align: center; line-height: 32px; }

  .contact-info { left: 559px; top: 604px; width: 490px; height: 234px; background: var(--teal); color: var(--white); font-size: 21px; line-height: 24px; }
  .contact-info h2 { position: absolute; left: 34px; top: 14px; font-weight: 600; font-size: 25px; }
  .contact-info .item { position: absolute; }

  .chat-now { left: 975px; top: 867px; width: 153px; height: 55px; border-radius: 10px; background: var(--chat); color: var(--white); font-family: "Oswald", sans-serif; font-weight: 300; font-size: 21px; display: flex; align-items: center; gap: 12px; padding-left: 9px; }

  .site-footer { left: 0; top: 905px; width: 1200px; height: 122px; background: var(--footer); color: var(--white); }
  .footer-links { position: absolute; left: 229px; top: 22px; font-family: "Oswald", sans-serif; font-weight: 300; font-size: 20px; }
  .socials { position: absolute; left: 812px; top: 24px; display: flex; gap: 10px; font-family: "Oswald", sans-serif; font-weight: 300; font-size: 14px; }
  .socials span { display: flex; align-items: center; gap: 4px; }
  .socials i { width: 8px; height: 8px; background: var(--white); display: inline-block; }
  .footer-rule { position: absolute; left: 43px; top: 65px; width: 1157px; height: 3px; background: var(--white); }
  .copyright { position: absolute; left: 0; width: 1120px; top: 85px; text-align: center; font-family: "EB Garamond", serif; font-size: 23px; }
</style>
</head>
<body>
<div class="page">
  <header class="site-header">
    <div class="abs brand"><span class="brand-mark"></span>PLINTHWAVE</div>
    <div class="abs header-phone">1-555-304-7718</div>
    <svg class="abs cart" width="30" height="28" viewBox="0 0 30 28" fill="none" stroke="#fff" stroke-width="2">
      <path d="M1 3h5l4 15h15l3-11H8"/><circle cx="12" cy="24" r="2"/><circle cx="23" cy="24" r="2"/>
      <path d="M10 11h17M11 15h15"/>
    </svg>
    <div class="abs cart-badge">1</div>
    <nav class="main-nav">
      <a href="#" style="left:698px">Products</a>
      <a href="#" style="left:802px">About</a>
      <a href="#" style="left:882px">Contact</a>
    </nav>
    <svg class="abs user" width="30" height="30" viewBox="0 0 30 30">
      <circle cx="15" cy="15" r="15" fill="#f5564a"/>
      <circle cx="15" cy="11" r="5" fill="none" stroke="#fff" stroke-width="2"/>
      <path d="M6 25c2-6 16-6 18 0" fill="none" stroke="#fff" stroke-width="2"/>
    </svg>
    <div class="abs user-name">Quartzel88</div>
  </header>

  <h1 class="abs page-title">Contact Us</h1>
  <div class="abs title-rule"></div>

  <div class="abs map" role="img" aria-label="Street map of the downtown waterfront area with the office location pinned"></div>
  <div class="abs address-card">
    <h3>Our address</h3>
    <p>48 Harbor Lane<br>2nd Floor, Suite 14<br>Bayview, CA 90000<br>support@plinthwavestudio.com<br>555-304-7718</p>
  </div>
  <svg class="abs address-tail" width="20" height="30" viewBox="0 0 20 30"><path d="M0 0h20L0 30z" fill="#20c7bd"/></svg>

  <form>
    <div class="abs field" style="left:157px;top:630px;width:156px;height:25px">Name:</div>
    <div class="abs field" style="left:332px;top:630px;width:157px;height:25px">Phone:</div>
    <div class="abs field" style="left:155px;top:666px;width:335px;height:25px;padding-top:5px">Email</div>
    <div class="abs field" style="left:157px;top:699px;width:333px;height:73px">Message:</div>
    <div class="abs submit">Submit</div>
  </form>

  <section class="abs contact-info">
    <h2>Contact Information</h2>
    <div class="item" style="left:9px;top:58px">Phone:<br>555-304-7718</div>
    <div class="item" style="left:12px;top:112px">Fax:<br>(555) 812 – 4490</div>
    <div class="item" style="left:243px;top:60px">Address:<br>48 Harbor Lane<br>2nd Floor, Suite 14<br>Bayview, CA 90000</div>
    <div class="item" style="left:19px;top:167px">E-mail:<br>support@plinthwavestudio.com</div>
  </section>

  <div class="abs chat-now">
    <svg width="40" height="32" viewBox="0 0 40 32" fill="none" stroke="#fff" stroke-width="3">
      <rect x="2" y="2" width="36" height="28" rx="3"/><path d="M3 4l17 14L37 4"/>
    </svg>
    Chat Now!
  </div>

  <footer class="abs site-footer">
    <div class="footer-links">About Contact Vellumly Laser Targeting Guide Questionnaires</div>
    <div class="socials">
      <span><i></i>Vellumly</span><span><i></i>Chirpset</span><span><i></i>Pictoraze</span>
    </div>
    <div class="footer-rule"></div>
    <div class="copyright">Copyright © 2018 Marrowfield, LLC - All rights reserved. Privacy Policy | Terms of Service</div>
  </footer>
</div>
</body>
</html>
```